I am writing a book called "SMILING OPENS EVERY DOOR "

I NEED A BOOK COVER FOR MY BOOK" SMILING OPENS EVERY DOOR"
so what was the question? " ( this in smaller font)

"Smiling Opens Every Door " will need to designed to eventually be a logo , banner and business card
COLOURS MAINLY ORANGE AND WHITE (with accents bright colour )

THE BOOK IS MY LAUGHTER JOURNEY AS A PERFORMER AND ADVENTURE INDIA LEARNING ABOUT LAUGHTER YOGA WHICH I WILL BE TEACHING

I do not want photos on the front cover ..
The look could be modern and eye-catching
I have also just been to India to learn Laughing Yoga with Dr Tobin Verhaal

Thank-you so much everyone for your brilliant designs . i am overwhelmed with your talent . i hope to work with you all again soon ! Marnie  

Target Market(s)

"Adults based in western speaking countries aged 25 to 60 that want to learn to laugh more
Also this book will be sold at my conference workshops

Industry/Entity Type

Business

Requirements
Must have
• ORANGE AND WHITE
CAN HAVE AQUA , HOT PINK , LIME GREEN, YELLOW ACCENTS

THESE WILL BE DIFFERENT AREAS WILL COVERING IN MY BOOK
EG LAUGHTER NAD BREAT CANCER ( PINK)
LAUGHTER NAD DEPRESSION ( BLUE)
LAUGHTER AND KIDS ( YELLOW)

NO Photos on front cover
Should not have
• No photos

```html
<!DOCTYPE html>
<html lang="en">
<head>
<meta charset="UTF-8">
<title>Smiling Opens Every Door – Book Cover</title>
<link rel="stylesheet" href="https://fonts.googleapis.com/css2?family=Caveat+Brush&family=Sriracha&family=Kaushan+Script&display=swap">
<style>
  :root {
    --paper-yellow: #f3bc06;
    --paper-light: #f7c81c;
    --paper-shade: #e8ac00;
    --title-white: #ffffff;
    --shadow-black: #111111;
    --author-black: #121212;
  }
  html, body {
    margin: 0;
    padding: 0;
    overflow: hidden;
  }
  .cover {
    position: relative;
    width: 846px;
    height: 1200px;
    overflow: hidden;
    background: var(--paper-yellow);
  }
  .paper-texture {
    position: absolute;
    inset: 0;
    background:
      radial-gradient(ellipse at 30% 20%, var(--paper-light) 0%, transparent 55%),
      radial-gradient(ellipse at 75% 80%, var(--paper-shade) 0%, transparent 60%),
      var(--paper-yellow);
  }
  .title {
    position: absolute;
    top: 190px;
    left: 0;
    width: 846px;
    margin: 0;
    text-align: center;
    font-family: "Caveat Brush", cursive;
    font-weight: 400;
    font-size: 138px;
    line-height: 126px;
    letter-spacing: 2px;
    color: var(--title-white);
    text-shadow: 4px 5px 0 var(--shadow-black);
  }
  .title-line {
    display: block;
  }
  .subtitle {
    position: absolute;
    top: 770px;
    left: 0;
    width: 846px;
    margin: 0;
    text-align: center;
    font-family: "Sriracha", cursive;
    font-size: 34px;
    color: var(--title-white);
  }
  .author {
    position: absolute;
    top: 1048px;
    left: 0;
    width: 846px;
    height: 56px;
  }
  .author-rule {
    position: absolute;
    top: 27px;
    height: 2px;
    background: var(--title-white);
  }
  .author-rule--left { left: 0; width: 246px; }
  .author-rule--right { right: 0; width: 246px; }
  .author-name {
    position: absolute;
    left: 0;
    width: 846px;
    top: 0;
    margin: 0;
    text-align: center;
    font-family: "Kaushan Script", cursive;
    font-size: 36px;
    line-height: 56px;
    color: var(--author-black);
  }
</style>
</head>
<body>
  <main class="cover">
    <div class="paper-texture" role="img" aria-label="Crumpled yellow paper texture background"></div>
    <h1 class="title">
      <span class="title-line">SMILING</span>
      <span class="title-line">OPENS</span>
      <span class="title-line">EVERY</span>
      <span class="title-line">DOOR</span>
    </h1>
    <p class="subtitle">So what was the question?</p>
    <div class="author">
      <span class="author-rule author-rule--left"></span>
      <p class="author-name">Marnie Hollis</p>
      <span class="author-rule author-rule--right"></span>
    </div>
  </main>
</body>
</html>
```